International Marketing Company - Web Design Project

kVesta is a well-funded start up in London developing an Online Marketing Platform for small businesses in Europe.

We require a large number of high quality business web designs for our business website builder. Our business websites are completely integrated into our Online Marketing systems and therefore it is important for designers to comply with our Design Guidelines.

This initial contest is a trial for us to open up the design process to top designers for the Builders vertical (e.g. Builders, Electricians, Plumbers, Flooring, etc.). We have implemented a base html structure and design and included them in the files.

Use your creativity to design new and fresh designs based on the included elements (e.g. testimonials, business description, etc).

We will award the stated prize money for the top three designs.

Any designers that submit designs we feel are of a high enough quality but do not make the top 3 could still be compensated and WILL be invited to participate in our next vertical competition.

Therefore, we encourage designers to submit as many designs as possible as we may award up to 25 designs.

Submissions will be reviewed daily and feedback provided where possible.

Designers who can also code will have the options to implement their designs for an additional fee.

Good luck!
Updates

There has been a mistake made in regard to the prize. Pixel Harbor should have it fixed soon.

1st place = £350
2nd place = £250
3rd Place = £150

Thanks,
Dorian
25/11/2011

UPDATE:

1st place will win £350
2nd place will win £250
3rd place will win £150

Everything else is as to the specification.

Thanks
Dorian

Target Market(s)

Builders, Electricians, Plumbers, Tradesman, Small construction companies

Industry/Entity Type

Business

Requirements
Must have
• Totally new designs based around the elements we want to show on each page.

We are looking for something different to the design we already have. But you can use that as a starting point.

Use the included files to see what is required for each page. Here is a brief outline:

Homepage - Testimonials, News, Business Description, Latest Projects and Call to action

About-Us - Team Summary, About the Business and a call to action

Projects Page - Project Details (Oage Title and description), Each project needs a title, content and 2 images.

Testimonials Page - The testifiers name and their comment

Contacts Page - Trovix Map, Company address, business hours, contact form and a call to action.

Please submit final designs in Photoshop or Fireworks format.

Each page has a set of elements. These element must feature in the design of that page. See supporting documents for page details.

All elements must be included in your design. Please do not add any extra element.

Professional look and feel
Nice to have
• Design variations:
Full width designs
Boxed Designs
With AND without carousels
OR static images
Good use of stock images.

Creative use of the elements, dont be restricted/influenced by the default design we have already

Designs based on the 960 grid

```html
<!DOCTYPE html>
<html lang="en">
<head>
<meta charset="utf-8">
<title>Ridgeway Builders</title>
<link href="https://fonts.googleapis.com/css2?family=Arimo:wght@400;700&display=swap" rel="stylesheet">
<style>
:root{
  --bg-dark:#141414;
  --bg-tile:#1c1c1c;
  --paper:#ffffff;
  --blue:#1aa3e6;
  --ink:#6f6f6f;
  --ink-soft:#8a8a8a;
  --name-grey:#b4b4b4;
  --rule:#9a9a9a;
  --nav:#000000;
  --orange:#f47b16;
  --orange-light:#ffa043;
}
*{margin:0;padding:0;box-sizing:border-box}
html,body{width:1162px;height:1200px;overflow:hidden;background:var(--bg-dark)}
body{font-family:"Arimo",Arial,sans-serif;color:var(--ink)}
.canvas{width:1162px;height:1200px;overflow:hidden;position:relative;
  background:
   repeating-linear-gradient(90deg,rgba(255,255,255,.03) 0 1px,transparent 1px 12px),
   repeating-linear-gradient(0deg,rgba(255,255,255,.03) 0 1px,transparent 1px 12px),
   radial-gradient(ellipse at 50% 40%,#2a2a2a,#0e0e0e 75%);}
.stage{position:absolute;left:0;top:0;width:1220px;height:1260px;transform:scale(.9525);transform-origin:0 0}
.abs{position:absolute}
.call{left:140px;top:6px;font-size:31px;color:var(--blue);letter-spacing:-1px;word-spacing:4px}
.admin{left:1012px;top:25px;font-size:12px;color:var(--blue)}
.page{left:140px;top:52px;width:942px;height:1148px;background:var(--paper)}
.brand{left:140px;top:225px;width:302px;text-align:center}
.brand-name{display:inline-flex;align-items:center;gap:10px;font-size:28px;color:#1c1c1c}
.brand-name i{display:inline-block;width:18px;height:18px;border-radius:50%;background:var(--blue)}
.tagline{margin-top:14px;font-size:14px;letter-spacing:1px;color:#111}
.hero{left:443px;top:60px;width:629px;height:308px;border:1px solid #ddd;
  background:linear-gradient(180deg,#ffffff,#eeeeee)}
.hero-photo{position:absolute;left:130px;top:20px;width:300px;height:275px;
  background:radial-gradient(ellipse at 50% 55%,#8aa6c6,#c8d4e0 55%,rgba(238,238,238,0) 75%)}
.dots{position:absolute;top:110px}
.dots.prev{left:35px}.dots.next{left:560px}
.quote-btn{position:absolute;left:432px;top:229px;width:194px;height:50px;border-radius:8px;
  background:linear-gradient(180deg,var(--orange-light),var(--orange));color:#fff;font-weight:700;font-size:20px;
  display:flex;align-items:center;padding-left:14px;gap:16px;box-shadow:0 6px 8px rgba(244,123,22,.25)}
.quote-btn span.arrow{width:30px;height:30px;border-radius:50%;background:#fff;display:flex;align-items:center;justify-content:center}
.nav{left:150px;top:376px;width:922px;height:48px;background:var(--nav);display:flex;align-items:center;padding-left:30px}
.nav a{color:#fff;font-weight:700;font-size:13px;letter-spacing:1px;text-decoration:none}
.nav a.current{color:var(--blue)}
.nav .sep{color:#fff;font-size:11px;margin:0 18px}
.section-title{font-size:20px;color:#6a6a6a;letter-spacing:-.5px;display:flex;align-items:flex-end;gap:6px;height:32px;border-bottom:3px solid var(--rule);padding-bottom:4px}
.col-left{left:150px;top:444px;width:290px}
.col-main{left:500px;top:444px;width:547px}
.quote{position:relative;padding-left:30px;margin-top:22px;font-size:12px;line-height:16px}
.quote .mark{position:absolute;left:0;top:-2px;font-size:36px;line-height:30px;color:var(--blue);font-family:Georgia,serif;font-weight:700}
.quote p{width:255px;text-align:justify;text-align-last:left}
.more{display:block;text-align:right;font-weight:700;color:var(--blue);font-size:12px;width:251px;margin-top:-2px}
.who{font-weight:700;font-size:14px;color:var(--name-grey);margin-top:2px}
.news-item{position:relative;padding-left:30px;font-size:12px;line-height:16px;margin-top:13px}
.news-item svg{position:absolute;left:4px;top:2px}
.news-item p{width:255px}
.news-item b{color:var(--blue);margin-left:10px}
.intro{margin-top:30px;font-size:14px;line-height:16px;color:#777;text-align:justify}
.intro + .intro{margin-top:16px}
.read-more{text-align:right;font-weight:700;color:var(--blue);font-size:14px;padding-right:8px}
.projects{display:flex;gap:6px;margin-top:15px}
.project{width:120px;text-align:center;font-size:10px;line-height:14px;color:#555}
.project .shot{height:164px;border:1px solid #888;box-shadow:2px 3px 5px rgba(0,0,0,.35);margin-bottom:4px}
.footer-rule{left:180px;top:1138px;width:857px;height:2px;background:var(--rule)}
.copyright{left:180px;top:1165px;font-size:12px;color:#777}
.footer-nav{left:659px;top:1165px;font-size:12px;color:#777;word-spacing:2px}
.footer-nav span{margin:0 12px}
</style>
</head>
<body>
<div class="canvas">
<div class="stage">
  <div class="abs call">Call: 020 7946 0321</div>
  <div class="abs admin">Admin Login</div>
  <div class="abs page"></div>

  <div class="abs brand">
    <div class="brand-name"><i></i>RIDGEWAY BUILDERS</div>
    <div class="tagline">Quick . Solid . Quality</div>
  </div>

  <div class="abs hero">
    <div class="hero-photo" role="img" aria-label="Builder in hard hat kneeling with a tape measure"></div>
    <svg class="dots prev" width="34" height="60" viewBox="0 0 34 60"><g fill="#c4c4c4"><circle cx="28" cy="5" r="3"/><circle cx="20" cy="13" r="3"/><circle cx="12" cy="21" r="3"/><circle cx="4" cy="29" r="3"/><circle cx="12" cy="37" r="3"/><circle cx="20" cy="45" r="3"/><circle cx="28" cy="53" r="3"/></g></svg>
    <svg class="dots next" width="34" height="60" viewBox="0 0 34 60"><g fill="#f3b51b"><circle cx="4" cy="5" r="3"/><circle cx="12" cy="13" r="3"/><circle cx="20" cy="21" r="3"/><circle cx="28" cy="29" r="3"/><circle cx="20" cy="37" r="3"/><circle cx="12" cy="45" r="3"/><circle cx="4" cy="53" r="3"/></g></svg>
    <div class="quote-btn">QUOTE NOW <span class="arrow"><svg width="16" height="14" viewBox="0 0 16 14"><path d="M1 5h8V1l6 6-6 6V9H1z" fill="#222"/></svg></span></div>
  </div>

  <nav class="abs nav">
    <a class="current">HOME</a><span class="sep">|</span>
    <a>ABOUT US</a><span class="sep">|</span>
    <a>TESTIMONIALS</a><span class="sep">|</span>
    <a>PORTFOLIO</a><span class="sep">|</span>
    <a>CONTACTS</a>
  </nav>

  <section class="abs col-left">
    <h2 class="section-title"><svg width="34" height="28" viewBox="0 0 34 28"><path d="M2 4a4 4 0 014-4h14a4 4 0 014 4v7a4 4 0 01-4 4h-9l-6 5v-5a4 4 0 01-3-4z" fill="#5aa9dc"/><path d="M14 12a4 4 0 014-4h12a4 4 0 014 4v6a4 4 0 01-3 4v5l-6-5h-7a4 4 0 01-4-4z" fill="#2b82c4"/></svg>Customers Say..</h2>

    <div class="quote"><span class="mark">“</span>
      <p>Ridgeway Construction are the best builders in Crawley. Ridgeway Construction are the best builders in Crawley. Ridgeway are the best builders in Crawley..</p>
      <span class="more">MORE&gt;&gt;</span>
      <div class="who">Mr. Halloran</div></div>
    <div class="quote"><span class="mark">“</span>
      <p>Ridgeway Construction are the best builders in Crawley. Ridgeway Construction are the best builders in Crawley. Ridgeway are the best builders in Crawley lorem ipsum ..</p>
      <span class="more">MORE&gt;&gt;</span>
      <div class="who">Mr. Halloran</div></div>
    <div class="quote"><span class="mark">“</span>
      <p>Ridgeway Construction are the best builders in Crawley. Ridgeway Construction are the best builders in Crawley. Ridgeway are the best builders in Crawley lorem ipsum ..</p>
      <span class="more">MORE&gt;&gt;</span>
      <div class="who">Mr. Halloran</div></div>

    <h2 class="section-title" style="margin-top:20px"><span role="img" aria-label="Newspaper icon" style="display:inline-block;width:34px;height:26px;background:linear-gradient(135deg,#d9e7f3,#5b8fc6);transform:rotate(-12deg)"></span>Latest News:</h2>
    <div class="news-item"><svg width="18" height="18" viewBox="0 0 18 18"><circle cx="8" cy="3" r="2" fill="#2b82c4"/><path d="M8 6v6M4 8l4-1 5 1M8 12l-3 5M8 12l3 5" stroke="#2b82c4" stroke-width="2" fill="none"/></svg>
      <p>Ridgeway Construction are the best builders in Crawley. Ridgeway Construction are the best builders in Crawley. Ridgeway are t . <b>MORE&gt;&gt;</b></p></div>
    <div class="news-item"><svg width="18" height="18" viewBox="0 0 18 18"><circle cx="8" cy="3" r="2" fill="#2b82c4"/><path d="M8 6v6M4 8l4-1 5 1M8 12l-3 5M8 12l3 5" stroke="#2b82c4" stroke-width="2" fill="none"/></svg>
      <p>Ridgeway Construction are the best builders in Crawley. Ridgeway Construction are the best builders in Crawley. Ridgeway are t . <b>MORE&gt;&gt;</b></p></div>
    <div class="news-item"><svg width="18" height="18" viewBox="0 0 18 18"><circle cx="8" cy="3" r="2" fill="#2b82c4"/><path d="M8 6v6M4 8l4-1 5 1M8 12l-3 5M8 12l3 5" stroke="#2b82c4" stroke-width="2" fill="none"/></svg>
      <p>Ridgeway Construction are the best builders in Crawley. Ridgeway Construction are the best builders in Crawley. Ridgeway are t . <b>MORE&gt;&gt;</b></p></div>
  </section>

  <section class="abs col-main">
    <h2 class="section-title"><span style="display:inline-block;width:30px;height:30px;background:var(--blue)"></span>Welcome to Ridgeway Builders</h2>
    <p class="intro">I am an experienced builder in Crawley. Ridgeway Construction have been based in Crawley for over 10 years. My team and I are proven, reliable builders based in Crawley. We've come across a lot in our time, so don't hesitate to get in touch about any building job in Crawley. I am an experienced builder in Crawley. Ridgeway Construction have been based in Crawley for over 10 years. My team and I are proven, reliable builders based in Crawley. We've come across a lot in our time, so don't hesitate to get in touch about any building job in Crawley.</p>
    <p class="intro">I am an experienced builder in Crawley. Ridgeway Construction have been based in Crawley for over 10 years. My team and I are proven, reliable builders based in Crawley. We've come across a lot in our time, so don't hesitate to get in touch about any building job in CrawleyI am an experienced builder in Crawley. Ridgeway Construction have been based in Crawley for over 10 years. My team and I are proven, reliable builders based in Crawley. We've come across a lot in our time, so don't hesitate to get in touch about any building job in CrawleyI am an experienced builder in Crawley. Ridgeway Construction have been based in Crawley for over 10 years. My team and I are proven, reliable builders based in Crawley. We've come across a lot in our time, so don't hesitate to get in touch about any building job in Crawley.</p>
    <div class="read-more">READ MORE&gt;&gt;</div>

    <h2 class="section-title" style="margin-top:32px"><span role="img" aria-label="Tools icon" style="display:inline-block;width:40px;height:34px;background:linear-gradient(135deg,#6fb6ea,#1f5f9e)"></span>Latest Projects</h2>
    <div class="projects">
      <div class="project"><div class="shot" role="img" aria-label="Restored lounge with leather armchairs" style="background:linear-gradient(180deg,#5a4030,#b07a4c 55%,#2d2520)"></div>House restoration in<br>Crawley</div>
      <div class="project"><div class="shot" role="img" aria-label="Loft dining room with laid table" style="background:linear-gradient(180deg,#b0783c,#e3c08c 50%,#f4efe6)"></div>Loft conversion near<br>Crawley</div>
      <div class="project"><div class="shot" role="img" aria-label="Bright painted kitchen interior" style="background:linear-gradient(180deg,#f2f2ef,#d8d4c8 55%,#b98a55)"></div>Home painting &amp;<br>Decorating in Crawley</div>
      <div class="project"><div class="shot" role="img" aria-label="Modern house extension interior" style="background:linear-gradient(180deg,#e8e6e0,#9a9890 50%,#141414)"></div>Beautiful house extension in<br>Crawley</div>
    </div>
  </section>

  <div class="abs footer-rule"></div>
  <div class="abs copyright">All Rights Reserved. Copyright © 2011</div>
  <div class="abs footer-nav">Home<span>|</span>About Us<span>|</span>Testimonials<span>|</span>Portfolio<span>|</span>Contact Us</div>
</div>
</div>
</body>
</html>
```